Buch-/eBook-Cover für Frauen zwischen 16-35
Zielgruppe
MLT/ Mellow Lantern Typesetting. Ich suche Unterstützung für die Erstellung eines Buchcovers für Frauen zwischen 16-35.
Aufgabenstellung
Ich habe eine Zusammenfassung des Projektes in dem beigefügten Word Dokument zusammen mit Beispielcovern, Covern der Konkurrenz etc.

```html
<!DOCTYPE html>
<html lang="de">
<head>
<meta charset="utf-8">
<title>Das bunte Mutproben-Buch für echte Komplizinnen – Cover</title>
<link rel="stylesheet" href="https://fonts.googleapis.com/css2?family=Bodoni+Moda:wght@400;500&family=Cormorant+Garamond:wght@500;600&display=swap">
<style>
  :root {
    --page-bg: #f4e3ee;
    --cover-pink: #f2a7c9;
    --cover-lilac: #c7b2d6;
    --cover-blue: #8fc3dc;
    --cover-peach: #f3b6a0;
    --title-yellow: #eef25a;
    --text-yellow: #e9ee6a;
    --hand-violet: #8a35c4;
    --hand-coral: #ff5a6e;
    --hand-orange: #ff9a3c;
  }
  * { box-sizing: border-box; margin: 0; padding: 0; }
  html, body { width: 1200px; height: 1200px; overflow: hidden; }
  body {
    background: var(--page-bg);
    display: flex;
    align-items: center;
    justify-content: center;
    gap: 80px;
  }
  .cover {
    position: relative;
    width: 430px;
    height: 640px;
    background:
      radial-gradient(ellipse at 15% 10%, rgba(242,167,201,.95), transparent 60%),
      radial-gradient(ellipse at 90% 25%, rgba(143,195,220,.95), transparent 55%),
      radial-gradient(ellipse at 30% 95%, rgba(243,182,160,.9), transparent 60%),
      linear-gradient(160deg, var(--cover-pink), var(--cover-lilac) 45%, var(--cover-blue) 75%, var(--cover-peach));
    box-shadow: 0 20px 40px rgba(120, 60, 100, .18);
    overflow: hidden;
  }
  .front-title {
    position: absolute;
    top: 52px;
    left: 0; right: 0;
    text-align: center;
    font-family: "Bodoni Moda", serif;
    font-weight: 400;
    font-size: 44px;
    line-height: 1.02;
    color: var(--title-yellow);
    letter-spacing: .5px;
  }
  .front-title .highlight { position: relative; display: inline-block; }
  .front-title .highlight svg {
    position: absolute;
    left: -30px; top: -6px;
    width: calc(100% + 60px); height: calc(100% + 12px);
    overflow: visible;
  }
  .front-subtitle {
    position: absolute;
    top: 300px;
    left: 70px;
    width: 200px;
    font-family: "Cormorant Garamond", serif;
    font-weight: 600;
    font-size: 11px;
    line-height: 1.3;
    text-transform: uppercase;
    color: var(--text-yellow);
  }
  .front-hands {
    position: absolute;
    left: 50px;
    top: 355px;
    width: 330px;
    height: 260px;
    border-radius: 40% 40% 20% 20%;
    background: linear-gradient(90deg, var(--hand-violet) 0%, #b04fd0 40%, var(--hand-coral) 60%, var(--hand-orange) 100%);
    opacity: .85;
  }
  .back-heading {
    position: absolute;
    top: 46px; left: 30px; right: 30px;
    text-align: center;
    font-family: "Bodoni Moda", serif;
    font-size: 20px;
    line-height: 1.15;
    color: var(--title-yellow);
  }
  .back-body {
    position: absolute;
    top: 150px; left: 42px; right: 42px;
    font-family: "Cormorant Garamond", serif;
    font-weight: 600;
    font-size: 12.5px;
    line-height: 1.55;
    text-transform: uppercase;
    color: var(--text-yellow);
    letter-spacing: .3px;
  }
  .back-body p + p { margin-top: 16px; }
  .back-emblem {
    position: absolute;
    left: 50%; bottom: 42px;
    transform: translateX(-50%);
    width: 44px; height: 48px;
    border-radius: 40%;
    background: linear-gradient(135deg, var(--hand-violet), var(--hand-coral) 55%, var(--hand-orange));
  }
</style>
</head>
<body>
  <section class="cover cover-front">
    <h1 class="front-title">
      DAS BUNTE<br>MUTPROBEN-<br>BUCH FÜR<br>
      <span class="highlight">ECHTE
        <svg viewBox="0 0 100 40" preserveAspectRatio="none" aria-hidden="true">
          <ellipse cx="50" cy="20" rx="49" ry="18" fill="none" stroke="#ffffff" stroke-width="0.6" vector-effect="non-scaling-stroke"/>
        </svg>
      </span><br>KOMPLIZINNEN
    </h1>
    <p class="front-subtitle">52 Wochen voller Spaß und neuer Erlebnisse</p>
    <div class="front-hands" role="img" aria-label="Illustration zweier Hände in Violett und Koralle, die sich mit den kleinen Fingern einhaken"></div>
  </section>

  <section class="cover cover-back">
    <h2 class="back-heading">Vom Alltag zu Abenteuer:<br>Entdecke die Magie<br>gemeinsamer Erlebnisse</h2>
    <div class="back-body">
      <p>Das Mutproben-Buch für echte Komplizinnen bietet euch 52 abwechslungsreiche Aktivitäten, die euch ein Jahr voller Spaß, Abenteuer und unvergesslicher Erinnerungen schenken, um eure Freundschaft für immer zu stärken.</p>
      <p>Von spannenden Outdoor-Abenteuern bis zu kreativen DIY-Projekten – jede Woche bringt die perfekte Aktivität, die eure Verbindung in eurem Alltag stärkt. Eure Freundschaft lacht gemeinsam und genießt die Kontraste miteinander.</p>
      <p>Entdeckt, wie viel Freude und Abwechslung das Leben bietet, wenn ihr es zusammen erlebt. Macht jede Woche zu etwas Besonderem – mit dem Mutproben-Buch für echte Komplizinnen!</p>
    </div>
    <div class="back-emblem" role="img" aria-label="Kleine Illustration zweier eingehakter Hände"></div>
  </section>
</body>
</html>
```